Harbor Vale needs a Business Card Design

We need a business card design for an Information Technology company based in Fairfax Virginia called Harbor Vale. We want the business card to use our logo colors. We need it to be double-sided. The business card needs to look professional but we would like it to be unique. You can get company information from our web site (http://www.harborvalellc.example).

Target Market(s)

Target market is Government Agencies and Business Professionals.

Industry/Entity Type

Business

Requirements
Must have
• Must have section for company name, company address, company URL, employee name, title, phone and email. Also must have company logo and space for entering logos.

```html
<!DOCTYPE html>
<html lang="en">
<head>
<meta charset="utf-8">
<title>Harbor Vale – Business Card</title>
<link rel="stylesheet" href="https://fonts.googleapis.com/css2?family=Questrial&display=swap">
<style>
  :root {
    --navy: #2b3a97;
    --azure: #137cc3;
    --white: #ffffff;
    --ink: #2b3a97;
    --backdrop: #eef0f4;
  }
  * { box-sizing: border-box; margin: 0; padding: 0; }
  html, body { width: 1200px; height: 784px; overflow: hidden; }
  body {
    background: var(--backdrop);
    font-family: "Questrial", "Century Gothic", sans-serif;
    display: flex;
    align-items: center;
    justify-content: center;
    gap: 40px;
  }
  .card {
    width: 560px;
    height: 320px;
    position: relative;
    overflow: hidden;
    box-shadow: 0 6px 18px rgba(20, 30, 70, .18);
  }

  /* Back side */
  .card-back { background: var(--azure); }
  .card-back .panel-left {
    position: absolute; left: 0; top: 0; bottom: 0; width: 230px;
    background: var(--navy);
  }
  .card-back .panel-band {
    position: absolute; left: 230px; top: 0; bottom: 0; width: 48px;
    background: var(--white);
  }
  .card-back .brand {
    position: absolute; left: 0; right: 0; top: 118px;
    display: flex; align-items: center; justify-content: center; gap: 16px;
  }
  .card-back .brand-square {
    width: 40px; height: 40px; background: var(--white);
  }
  .card-back .brand-name {
    color: var(--white); font-size: 44px; letter-spacing: 1px;
    background: var(--navy); padding: 2px 12px;
  }
  .card-back .web {
    position: absolute; right: 22px; bottom: 40px;
    color: var(--white); font-size: 20px;
  }

  /* Front side */
  .card-front { background: var(--white); }
  .card-front .holder {
    position: absolute; right: 24px; top: 22px; text-align: right;
    color: var(--ink);
  }
  .card-front .holder-name { font-size: 15px; }
  .card-front .holder-title { font-size: 13px; color: var(--azure); }
  .card-front .brand {
    position: absolute; left: 34px; top: 74px;
    display: flex; align-items: center; gap: 16px;
  }
  .card-front .brand-square { width: 46px; height: 46px; background: var(--navy); }
  .card-front .brand-name { color: var(--navy); font-size: 38px; line-height: 1; }
  .card-front .tagline {
    color: var(--navy); font-size: 11px; letter-spacing: .8px;
    text-transform: uppercase; margin-top: 4px;
  }
  .card-front .stripe {
    position: absolute; left: 0; right: 0; top: 152px; height: 10px;
    background: var(--azure);
  }
  .card-front .contact-band {
    position: absolute; left: 0; right: 0; top: 162px; bottom: 0;
    background: var(--navy);
    padding: 16px 0 0 30px;
  }
  .contact-list { list-style: none; }
  .contact-list li {
    display: flex; align-items: center; gap: 12px;
    color: var(--white); font-size: 19px; line-height: 26px;
  }
  .contact-list svg { width: 18px; height: 18px; fill: var(--azure); flex: none; }
</style>
</head>
<body>

  <section class="card card-back" aria-label="Business card back">
    <div class="panel-left"></div>
    <div class="panel-band"></div>
    <div class="brand">
      <span class="brand-square"></span>
      <span class="brand-name">Harbor Vale</span>
    </div>
    <p class="web">www.harborvalellc.example</p>
  </section>

  <section class="card card-front" aria-label="Business card front">
    <div class="holder">
      <p class="holder-name">Dana Whitfield</p>
      <p class="holder-title">Manager</p>
    </div>
    <div class="brand">
      <span class="brand-square"></span>
      <div>
        <p class="brand-name">Harbor Vale</p>
        <p class="tagline">Turning Ideas into Solutions</p>
      </div>
    </div>
    <div class="stripe"></div>
    <div class="contact-band">
      <ul class="contact-list">
        <li>
          <svg viewBox="0 0 24 24" aria-hidden="true"><path d="M6.6 10.8a15.1 15.1 0 0 0 6.6 6.6l2.2-2.2a1 1 0 0 1 1-.25 11.4 11.4 0 0 0 3.6.57 1 1 0 0 1 1 1V20a1 1 0 0 1-1 1A17 17 0 0 1 3 4a1 1 0 0 1 1-1h3.5a1 1 0 0 1 1 1c0 1.25.2 2.45.57 3.57a1 1 0 0 1-.25 1z"/></svg>
          555.010.4420
        </li>
        <li>
          <svg viewBox="0 0 24 24" aria-hidden="true"><path d="M7 1h10a2 2 0 0 1 2 2v18a2 2 0 0 1-2 2H7a2 2 0 0 1-2-2V3a2 2 0 0 1 2-2zm0 3v14h10V4zm5 15.5a1.2 1.2 0 1 0 0 2.4 1.2 1.2 0 0 0 0-2.4z"/></svg>
          555.014.7731
        </li>
        <li>
          <svg viewBox="0 0 24 24" aria-hidden="true"><path d="M6 2h12v6H6zM4 9h16a2 2 0 0 1 2 2v7h-4v4H6v-4H2v-7a2 2 0 0 1 2-2zm4 7v4h8v-4z"/></svg>
          555.019.2286
        </li>
        <li>
          <svg viewBox="0 0 24 24" aria-hidden="true"><path d="M2 5h20v14H2zm2 2v.5l8 5.5 8-5.5V7l-8 5.2z"/></svg>
          info@harborvalellc.example
        </li>
        <li>
          <svg viewBox="0 0 24 24" aria-hidden="true"><path d="M12 3l10 9h-3v9h-5v-6h-4v6H5v-9H2z"/></svg>
          1480 Meridian Ave, Suite 310
        </li>
      </ul>
    </div>
  </section>

</body>
</html>
```